CREATE R&B MIXTAPE COVER !!
Hi , my name is Darnell , and I want you to create a cover for my music mixtape.
The name of the mixtape is Sombrelia , and has these types of music :
- R&B
- Hiphop
- Afrohouse
- Dancehall
- Reggaeton
In the attachments you’ll find two backgrounds. One with a lightning bolt , and a grey one with a stroke in the middle. I like both very much , but don’t know which one to choose. That’s why I want to compare the end results of both , and then make a decision. Below you’ll find instructions for both backgrounds.
If you think you can make something better for me , you can also try to do your own thing , and use your own background for example.
Instructions for the first background ( Lightning bolt )
I would like you to design my name ‘Darnell’ into / onto the lightning bolt. I want the lightning bolt + my name to be my DJ Logo , but my name doesn’t have to be in very big letters. Sombrelia is the name of the mixtape and has to be in big letters. I was thinking above the logo.
Then there are 2 remaining sentences : ‘Mixed by DJ Darnell’ and ‘Mixtape Volume 1’. These two sentences have to be smaller than ‘Sombrelia’. You can put them under the logo.
Instructions for the second background ( Grey )
I would like you to create a logo of my whole name ‘Darnell’ Or just with the letter D. You can put the logo above the stroke.
The mixtape name ‘Sombrelia’ has to be in the middle in big letters.
Then there are 2 remaining sentences : ‘Mixed by DJ Darnell’ and ‘Mixtape Volume 1’. These two have to be smaller than ‘Sombrelia’ in the middle. I want these sentences below.
Use your imagination with the name Sombrelia , the two sentences and the logo. I want it to look professional and unique.
Kind regards ,
Darnell

```html
<!DOCTYPE html>
<html lang="en">
<head>
<meta charset="utf-8">
<title>Sombrelia – Mixtape Volume 1</title>
<link href="https://fonts.googleapis.com/css2?family=Rubik+Dirt&family=Michroma&display=swap" rel="stylesheet">
<style>
  :root {
    --night: #070b10;
    --sky-top: #141c2a;
    --sky-low: #9a3a1c;
    --band: #050505;
    --sea-top: #3f9a22;
    --sea-low: #0b2628;
    --title-green: #57b52a;
    --title-yellow: #e4d21f;
    --title-orange: #f07a1a;
    --title-red: #d9321c;
    --caption: #e9e9e9;
    --mark: #9a9a9a;
  }
  html, body {
    margin: 0;
    padding: 0;
    overflow: hidden;
    background: var(--night);
  }
  .cover {
    position: relative;
    width: 1200px;
    height: 802px;
    overflow: hidden;
    background: var(--night);
  }
  .sky-scene {
    position: absolute;
    left: 0; top: 0;
    width: 1200px; height: 276px;
    background: linear-gradient(180deg, var(--sky-top) 0%, var(--sky-low) 100%);
  }
  .dark-band {
    position: absolute;
    left: 0; top: 276px;
    width: 1200px; height: 216px;
    background: var(--band);
  }
  .sea-scene {
    position: absolute;
    left: 0; top: 492px;
    width: 1200px; height: 310px;
    background: linear-gradient(180deg, var(--sea-top) 0%, var(--sea-low) 100%);
  }
  .dj-mark {
    position: absolute;
    left: 0; top: 128px;
    width: 1200px;
    display: flex;
    justify-content: center;
    align-items: center;
    gap: 22px;
  }
  .dj-mark__dot {
    width: 110px; height: 110px;
    border-radius: 50%;
    background: var(--mark);
  }
  .dj-mark__name {
    font-family: "Michroma", sans-serif;
    font-size: 38px;
    color: var(--mark);
    letter-spacing: 3px;
  }
  .title {
    position: absolute;
    left: 0; top: 312px;
    width: 1200px;
    margin: 0;
    text-align: center;
    font-family: "Rubik Dirt", sans-serif;
    font-weight: 400;
    font-size: 146px;
    line-height: 1;
    letter-spacing: 1px;
    background: linear-gradient(90deg, var(--title-green) 18%, var(--title-green) 32%, var(--title-yellow) 55%, var(--title-orange) 74%, var(--title-red) 84%);
    -webkit-background-clip: text;
    background-clip: text;
    color: transparent;
  }
  .credits {
    position: absolute;
    left: 0; top: 502px;
    width: 1200px;
    margin: 0;
    text-align: center;
    font-family: "Michroma", sans-serif;
    font-size: 14px;
    color: var(--caption);
    letter-spacing: 0.5px;
  }
</style>
</head>
<body>
  <main class="cover">
    <div class="sky-scene" role="img" aria-label="Photograph of a sunset with an orange sun and dark clouds over the horizon"></div>
    <div class="dark-band"></div>
    <div class="sea-scene" role="img" aria-label="Photograph of a green glowing sea surface under a dark sky"></div>

    <div class="dj-mark">
      <span class="dj-mark__dot"></span>
      <span class="dj-mark__name">Darnell</span>
    </div>

    <h1 class="title">Sombrelia</h1>
    <p class="credits">Mixtape Volume 1 - Mixed by DJ Darnell</p>
  </main>
</body>
</html>
```